TrellanVita Website - Biologics storage and handling

I would like a beginning design on a website for TrellanVita:

A Boston-based company dedicated to sourcing, storing, and supplying biologic materials of all kinds to the life sciences and scientific markets. From starting reagents, to basic and intermediate materials, to final synthesized and engineered products, we provide value throughout the biologics supply chain. TrellanVita provides backup, overflow, emergency, and stocking storage solutions to companies on a temporary or permanent basis. Life sciences companies can take advantage of the fact that the company is located in the middle of the Boston/Cambridge biotechnology corridor in order to have quick and efficient access to their cold chain materials. Out of state companies can leverage TrellanVita’s location for efficient distribution of materials to partner and client organizations. We also provide other value added services to organizations that do not have the local manpower, such as sourcing, supply, and distribution of materials.

The design should be mostly a white background with clean, linear, geometric colors added in according to the blue and orange color scheme represented in the corporate logo attached.

The website needs to communicate reliable service and provide the concept of a company dedicated to handling and providing client biological samples in a secure and efficient manner.

Some local competitors are:
1. Korbel BioWorks: www.korbelbw.example
2. LabVault: www.labvault-store.example

From a design perspective, I like the Halvenor Thera website:

www.halvenorthera.example

Target Market(s)

Life sciences companies and other organizations

Industry/Entity Type

Biotechnology

Coding

Coded - Design and coding required

Number of Pages Required

5+ page

Font styles to use
Sans Serif

Colors
3176b5
0455a3
f37122

Requirements
Must have
• Tabs for pages:
About - Company information.
Platform - Inventory and sample management cloud platform; temperature profiling, logging, and reporting.
Services - Refrigeration and freezing services for biological samples, logistics services, sourcing services, courier services.
Updates - News, events, blog.
Login portal - Entry point for getting into platform. Maybe some freemium content here.
Nice to have
• Please be creative about website page sections, vibrant colors according to my established color scheme, and clean, linear, geometric shapes. I would like a white background with nice colors, clean lines and borders, and a very contemporary look. I want o
Should not have
• This is not a Business to Consumer business. This is a Business to Business enterprise. There should not be consumer oriented language. It is more about service and relationship management.

```html
<!DOCTYPE html>
<html lang="en">
<head>
<meta charset="utf-8">
<title>TrellanVita — Biologics Storage and Handling</title>
<link rel="stylesheet" href="https://fonts.googleapis.com/css2?family=Lato:wght@300;400;700;900&family=Raleway:wght@300;400;600&display=swap">
<style>
:root{
  --blue:#0455a3;
  --blue-mid:#3176b5;
  --blue-deep:#0a3a86;
  --navy:#0b3f8f;
  --orange:#f37122;
  --ink:#2b2f38;
  --grey:#8a8f99;
  --light:#f1f3f7;
  --white:#ffffff;
}
*{margin:0;padding:0;box-sizing:border-box}
html,body{width:1200px;height:3232px;overflow:hidden}
body{font-family:"Lato",sans-serif;color:var(--ink);background:var(--white);position:relative}
.abs{position:absolute}

/* hero */
.hero{position:absolute;left:0;top:0;width:1200px;height:1010px;overflow:hidden}
.hero-visual{position:absolute;inset:0;background:
  radial-gradient(ellipse 420px 380px at 860px 380px,rgba(140,150,200,.55),transparent 70%),
  radial-gradient(ellipse 300px 260px at 180px 700px,rgba(90,170,230,.45),transparent 70%),
  linear-gradient(160deg,#0d2f78 0%,#1553a8 45%,#2d7cc6 75%,#1a4b9a 100%)}
.hero-structure{position:absolute;left:640px;top:150px;width:480px;height:560px;
  background:linear-gradient(135deg,rgba(243,113,34,.35),rgba(180,140,170,.35) 50%,rgba(60,90,170,.3));
  clip-path:polygon(50% 0,100% 25%,100% 75%,50% 100%,0 75%,0 25%)}
.nav{position:absolute;top:0;left:0;width:1200px;height:110px}
.brand{position:absolute;left:134px;top:46px;display:flex;align-items:center;gap:12px}
.brand-square{width:22px;height:22px;background:var(--white)}
.brand-name{font-family:"Raleway",sans-serif;font-weight:400;font-size:32px;color:var(--white);letter-spacing:1px}
.menu{position:absolute;right:140px;top:58px;display:flex;align-items:center;gap:30px}
.menu a{font-size:15px;font-weight:700;color:var(--white);text-decoration:none;letter-spacing:.5px}
.menu a.active{border-bottom:2px solid var(--white);padding-bottom:3px}
.login{background:var(--orange);padding:10px 14px 10px 22px;display:flex;align-items:center;gap:14px}
.arrow-dot{width:24px;height:24px;border-radius:50%;background:var(--white);display:flex;align-items:center;justify-content:center}
.hero-title{position:absolute;left:150px;top:300px;font-family:"Raleway",sans-serif;font-weight:300;font-size:76px;color:var(--white);letter-spacing:3px}
.hero-sub{position:absolute;left:150px;top:405px;font-size:36px;line-height:48px;color:var(--white);font-weight:400}
.btn{background:var(--orange);color:var(--white);font-size:13px;font-weight:700;letter-spacing:.5px;display:inline-flex;align-items:center;gap:12px;padding:12px 14px 12px 18px}
.hero-btn{position:absolute;left:150px;top:530px}
.hero-wave{position:absolute;left:0;top:820px}

/* about */
.about-title{position:absolute;left:146px;top:1070px;font-size:58px;font-weight:700;line-height:62px;color:var(--blue)}
.about-title span{color:var(--orange);font-weight:400;display:block}
.about-mark{position:absolute;left:150px;top:1215px;width:74px;height:74px;background:var(--blue)}
.about-text{position:absolute;left:545px;top:1060px;width:520px;font-size:14px;line-height:24px;color:var(--grey)}

/* activities */
.activities{position:absolute;left:0;top:1330px;width:1200px;height:720px}
.section-title{position:absolute;left:0;width:1200px;text-align:center;font-size:54px;font-weight:700;color:var(--blue)}
.section-title span{color:var(--orange);font-weight:400}
.diamond{position:absolute;width:214px;height:214px;transform:rotate(45deg);overflow:hidden;border:2px solid rgba(255,255,255,.6)}
.diamond.source{left:193px;top:1626px;background:linear-gradient(135deg,#2c6fbd,#0a4494 60%,#5aa0da)}
.diamond.store{left:488px;top:1600px;width:232px;height:232px;background:linear-gradient(135deg,#1c5fb0,#0b3f8f 55%,#3b8ad0);box-shadow:0 10px 30px rgba(0,40,100,.35)}
.diamond.supply{left:793px;top:1626px;background:linear-gradient(135deg,#3a7fc9,#0d4a9a 60%,#6aa9de)}
.activity-text{position:absolute;width:230px;text-align:center;color:var(--white)}
.activity-text h3{font-size:27px;font-weight:700;letter-spacing:1px;margin-bottom:10px}
.activity-text p{font-size:12px;line-height:17px}

/* news */
.news-card{position:absolute;top:2155px;width:290px}
.news-img{width:290px;height:178px;position:relative}
.news-date{position:absolute;left:0;bottom:0;background:var(--orange);color:var(--white);font-size:11px;font-weight:700;padding:6px 12px}
.news-card h4{font-size:18px;font-weight:700;color:var(--ink);margin:16px 0 10px}
.news-card p{font-size:12px;line-height:18px;color:var(--grey);margin-bottom:12px}
.read-more{font-size:11px;font-weight:900;color:var(--orange);letter-spacing:.5px}

/* contact */
.contact-bg{position:absolute;left:0;top:2450px}
.contact-card{position:absolute;left:236px;top:2590px;width:730px;height:352px;background:var(--white);box-shadow:0 10px 30px rgba(0,30,80,.2)}
.contact-info{position:absolute;left:0;top:0;width:262px;height:352px;background:var(--orange);padding:30px 28px;color:var(--white)}
.contact-info h5{font-size:17px;font-weight:700;letter-spacing:1px;margin-bottom:28px}
.info-row{display:flex;gap:14px;margin-bottom:24px}
.info-row b{display:block;font-size:12px;letter-spacing:.5px;margin-bottom:4px}
.info-row span{font-size:11px;line-height:16px}
.form{position:absolute;left:290px;top:28px;width:410px}
.form h5{font-size:17px;font-weight:700;color:var(--ink);margin-bottom:20px}
.field{border-bottom:1px solid #d4d8df;font-size:11px;color:var(--grey);padding:10px 0 8px;margin-bottom:8px}
.field.tall{height:78px}
.form-foot{display:flex;justify-content:space-between;align-items:center;margin-top:18px}
.check{display:flex;align-items:center;gap:10px;border:1px solid #d4d8df;background:#f9f9f9;padding:10px 14px;font-size:11px;color:var(--ink)}
.check i{width:18px;height:18px;border:2px solid #bfc4cc;background:var(--white);display:block}

/* footer */
.footer-nav{position:absolute;left:0;top:3020px;width:1200px;display:flex;justify-content:center;gap:36px}
.footer-nav a{color:var(--white);font-size:16px;font-weight:700;text-decoration:none;letter-spacing:.5px}
.copyright{position:absolute;left:0;top:3090px;width:1200px;text-align:center;font-size:12px;color:rgba(255,255,255,.85)}
.social{position:absolute;left:0;top:3130px;width:1200px;display:flex;justify-content:center;gap:12px}
.social i{width:28px;height:28px;border-radius:50%;background:var(--white);display:block}
</style>
</head>
<body>

<header class="hero">
  <div class="hero-visual" role="img" aria-label="Blue laboratory background with magnified cells and a layered geometric crystal structure"></div>
  <div class="hero-structure" role="img" aria-label="Layered geometric structure illustration"></div>
  <nav class="nav">
    <div class="brand"><span class="brand-square"></span><span class="brand-name">TrellanVita</span></div>
    <div class="menu">
      <a class="active" href="#">ABOUT</a>
      <a href="#">PLATFORM</a>
      <a href="#">SERVICES</a>
      <a href="#">UPDATES</a>
      <a class="login" href="#">LOGIN PORTAL <span class="arrow-dot"><svg width="12" height="12" viewBox="0 0 12 12"><path d="M2 6h7M6 3l3 3-3 3" stroke="#0455a3" stroke-width="2" fill="none"/></svg></span></a>
    </div>
  </nav>
  <h1 class="hero-title">TrellanVita</h1>
  <p class="hero-sub">We are a Biologics storage and<br>Handling company</p>
  <a class="btn hero-btn">GET STARTED
    <svg width="12" height="12" viewBox="0 0 12 12"><path d="M2 6h7M6 3l3 3-3 3" stroke="#fff" stroke-width="2" fill="none"/></svg></a>
  <svg class="hero-wave" width="1200" height="190" viewBox="0 0 1200 190">
    <path d="M0 120 C250 40 420 190 700 130 C900 85 1050 40 1200 70 L1200 190 L0 190Z" fill="#0455a3" opacity=".6"/>
    <path d="M0 150 C260 70 430 200 700 150 C900 110 1050 70 1200 95" stroke="#f37122" stroke-width="6" fill="none"/>
    <path d="M0 165 C260 90 430 210 700 165 C900 125 1050 90 1200 112 L1200 190 L0 190Z" fill="#ffffff"/>
  </svg>
</header>

<section>
  <h2 class="about-title">About<span>TrellanVita</span></h2>
  <div class="about-mark"></div>
  <p class="about-text">TrellanVita is dedicated to sourcing, storing, and supplying biologic materials of all kinds to the life sciences and scientific markets. From starting reagents, to basic and intermediate materials, to final synthesized and engineered products, we provide value throughout the biologics supply chain. TrellanVita provides backup, overflow, emergency, and stocking storage solutions to companies on a temporary or permanent basis. Life sciences companies can take advantage of the fact that the company is located in the middle of the Boston/Cambridge biotechnology corridor in order to have quick and efficient access to their cold chain materials. Out of state companies can leverage TrellanVita’s location for efficient distribution of materials to partner and client organizations. We also provide other value added services to organizations that do not have the local manpower, such as sourcing, supply, and distribution of materials.</p>
</section>

<section class="activities">
  <svg class="abs" style="left:0;top:0" width="1200" height="720" viewBox="0 0 1200 720">
    <path d="M0 40 C300 -10 700 10 1200 60 L1200 660 C800 700 400 720 0 680Z" fill="#f1f3f7"/>
  </svg>
  <h2 class="section-title" style="top:62px">TrellanVita <span>Activities</span></h2>
</section>
<div class="diamond source" role="img" aria-label="Laboratory sourcing image tinted blue"></div>
<div class="diamond store" role="img" aria-label="Cold storage image tinted blue"></div>
<div class="diamond supply" role="img" aria-label="Supply logistics image tinted blue"></div>
<div class="activity-text" style="left:185px;top:1680px"><h3>SOURCE</h3><p>Reagents, intermediate and final biologic materials found for your teams.</p></div>
<div class="activity-text" style="left:489px;top:1660px"><h3>STORE</h3><p>Cold chain storage of biologic samples on a temporary or permanent basis, monitored daily.</p></div>
<div class="activity-text" style="left:785px;top:1680px"><h3>SUPPLY</h3><p>Efficient distribution of materials to partner and client sites.</p></div>

<section>
  <h2 class="section-title" style="top:2045px;color:var(--blue)">Latest <span>News</span></h2>
  <article class="news-card" style="left:140px">
    <div class="news-img" role="img" aria-label="News image of a glowing DNA strand" style="background:linear-gradient(135deg,#0b3a7a,#2a8fd0 50%,#c8b640)"><span class="news-date">12 MARCH 2020</span></div>
    <h4>Um quia dolor sit ametonsecte</h4>
    <p>Cold chain update on storage capacity expansion for partner teams this spring season.</p>
    <span class="read-more">READ MORE</span>
  </article>
  <article class="news-card" style="left:455px">
    <div class="news-img" role="img" aria-label="News image of cells under a microscope" style="background:linear-gradient(135deg,#0e5e7a,#1ea3b0 50%,#c23a4a)"><span class="news-date">12 MARCH 2020</span></div>
    <h4>Um quia dolor sit ametonsecte</h4>
    <p>New temperature logging reports now available inside the client platform dashboard.</p>
    <span class="read-more">READ MORE</span>
  </article>
  <article class="news-card" style="left:770px">
    <div class="news-img" role="img" aria-label="News image of red blood cells" style="background:linear-gradient(135deg,#7a1f5a,#c44a7a 50%,#3a5fb0)"><span class="news-date">12 MARCH 2020</span></div>
    <h4>Um quia dolor sit ametonsecte</h4>
    <p>Meet our courier and sourcing team at the regional biotech forum next month.</p>
    <span class="read-more">READ MORE</span>
  </article>
</section>

<svg class="contact-bg" width="1200" height="782" viewBox="0 0 1200 782">
  <path d="M0 210 C200 150 350 230 520 250 C800 280 1000 200 1200 220 L1200 782 L0 782Z" fill="#0455a3"/>
  <path d="M0 250 C220 200 380 280 560 290 C820 305 1020 250 1200 260 L1200 782 L0 782Z" fill="#0b3f8f"/>
</svg>

<section class="contact-card">
  <div class="contact-info">
    <h5>GET IN TOUCH</h5>
    <div class="info-row">
      <svg width="16" height="20" viewBox="0 0 16 20"><path d="M8 0C3.6 0 0 3.4 0 7.7 0 13 8 20 8 20s8-7 8-12.3C16 3.4 12.4 0 8 0z" fill="#fff"/><circle cx="8" cy="7.5" r="3" fill="#f37122"/></svg>
      <div><b>ADDRESS</b><span>14 Corvane Street,<br>Unit 2, Eastbrook</span></div>
    </div>
    <div class="info-row">
      <svg width="16" height="18" viewBox="0 0 16 18"><path d="M3 1l3 0 1.5 4-2 1.5c1 2.2 2.6 3.8 4.8 4.8L12 9.3l4 1.5V14c0 1.5-1.2 2.6-2.6 2.4C6.8 15.6 1.4 10.2.6 3.6.4 2.2 1.5 1 3 1z" fill="#fff"/></svg>
      <div><b>PHONE</b><span>+1 555 010 0142</span></div>
    </div>
    <div class="info-row">
      <svg width="18" height="14" viewBox="0 0 18 14"><rect width="18" height="14" fill="#fff"/><path d="M1 1l8 6 8-6" stroke="#f37122" stroke-width="1.6" fill="none"/></svg>
      <div><b>EMAIL</b><span>hello@trellanvita.example</span></div>
    </div>
  </div>
  <div class="form">
    <h5>LET'S TALK</h5>
    <div class="field">Enter Name</div>
    <div class="field">Email Address</div>
    <div class="field tall">Message</div>
    <div class="form-foot">
      <div class="check"><i></i>I'm not a robot<span style="width:22px;height:22px;background:#d4d8df;margin-left:30px"></span></div>
      <a class="btn">SUBMIT <span class="arrow-dot"><svg width="12" height="12" viewBox="0 0 12 12"><path d="M2 6h7M6 3l3 3-3 3" stroke="#f37122" stroke-width="2" fill="none"/></svg></span></a>
    </div>
  </div>
</section>

<footer>
  <nav class="footer-nav">
    <a href="#">ABOUT</a><a href="#">PLATFORM</a><a href="#">SERVICES</a><a href="#">UPDATES</a><a href="#">LOGIN PORTAL</a>
  </nav>
  <p class="copyright">© Copyright 2020 TrellanVita. All Rights Reserved. | Privacy policy</p>
  <div class="social"><i></i><i></i><i></i><i></i><i></i></div>
</footer>

</body>
</html>
```